Entrepreneur Podcast Cover Graphic Design

My wife and I just launched our podcast but we don't like the current cover. We want a new cover designed so it stands out and reflects the professionalism of our podcast. Attached is our current podcast cover design. We'd like to have it read "Rob & Mireya Interview Entrepreneurs on TOUGH DECISIONS" - We'd also like to feature somehow that we have daily tips included.

Target Market(s)

entrepreneurs,business owners,start ups

Industry/Entity Type

Entrepreneur

Font styles to use
Sans Serif

Colors
0355a3
f37122
9bcb3c
fbed22
ec1f27

Requirements
Must have
• Our names listed: Rob & Mireya
Nice to have
• dark, bold colored background with an outline around the edge
Should not have
• no cartoons, no profanity

```html
<!DOCTYPE html>
<html lang="en">
<head>
<meta charset="utf-8">
<title>Rob &amp; Mireya Podcast Cover</title>
<link rel="stylesheet" href="https://fonts.googleapis.com/css2?family=Roboto:wght@300;700&display=swap">
<style>
  :root {
    --photo-light: #c9ccd0;
    --photo-mid: #5b6470;
    --photo-dark: #1d1a19;
    --band-top: #0a57a9;
    --band-bottom: #034592;
    --text: #ffffff;
    --tick: #ec1f27;
  }
  html, body {
    margin: 0;
    padding: 0;
    width: 1200px;
    height: 1200px;
    overflow: hidden;
    background: #0a57a9;
  }
  .cover {
    position: relative;
    width: 1200px;
    height: 1200px;
    overflow: hidden;
    font-family: "Roboto", Arial, sans-serif;
    color: var(--text);
  }
  .cover__photo {
    position: absolute;
    left: 0;
    top: 0;
    width: 1200px;
    height: 582px;
    background:
      linear-gradient(180deg, rgba(29,26,25,0) 40%, rgba(29,26,25,0.85) 82%, var(--photo-dark) 100%),
      linear-gradient(90deg, #1b2a38 0%, var(--photo-light) 22%, #e6e7e8 50%, #9fb3c6 78%, #7a4a3e 100%);
  }
  .cover__hosts {
    position: absolute;
    left: 81px;
    top: 338px;
    margin: 0;
    font-weight: 300;
    font-size: 90px;
    line-height: 112px;
    letter-spacing: -0.5px;
  }
  .cover__band {
    position: absolute;
    left: 0;
    top: 582px;
    width: 1200px;
    height: 618px;
    background: linear-gradient(180deg, var(--band-top), var(--band-bottom));
  }
  .cover__notch {
    position: absolute;
    left: 558px;
    top: 581px;
    width: 84px;
    height: 42px;
  }
  .cover__title {
    position: absolute;
    left: 78px;
    top: 640px;
    margin: 0;
    font-weight: 700;
    font-size: 184px;
    line-height: 174px;
    letter-spacing: -3px;
    text-transform: uppercase;
    white-space: nowrap;
  }
  .cover__tips {
    position: absolute;
    left: 84px;
    top: 1016px;
    display: flex;
    align-items: center;
    gap: 42px;
    font-weight: 300;
    font-size: 82px;
    line-height: 1;
    letter-spacing: -0.5px;
  }
  .cover__tick {
    width: 76px;
    height: 60px;
  }
</style>
</head>
<body>
  <div class="cover">
    <div class="cover__photo" role="img" aria-label="Photo of business people in silhouette talking by office windows with a city skyline behind"></div>
    <p class="cover__hosts">Rob &amp; Mireya Interview<br>Entrepreneurs on</p>
    <div class="cover__band"></div>
    <svg class="cover__notch" viewBox="0 0 84 42" aria-hidden="true">
      <polygon points="0,0 84,0 42,42" fill="#1d1a19"/>
    </svg>
    <h1 class="cover__title">Tough<br>Decisions!</h1>
    <div class="cover__tips">
      <svg class="cover__tick" viewBox="0 0 76 60" aria-hidden="true">
        <path d="M2 30 L26 54 L74 4" fill="none" stroke="var(--tick)" stroke-width="9" stroke-linejoin="miter"/>
      </svg>
      <span>INCLUDES DAILY TIPS</span>
    </div>
  </div>
</body>
</html>
```